Cloud-based Health 2.0 Web Site

We need the overall look and feel for a new cloud-based Health 2.0 web site where health professionals can manage and interact with their patients/clients.

The plan is to generate a landing page that can grab the attention of health professionals (doctors, nurses, personal trainers, etc...). This page should have an attractive "Sign Up for Free" or similar button/message, as well as a login section for users already registered. We currently have a view on having a number of messages displayed, either as a slider or as separate areas on the page (decision is up for grabs).

Secondly, we need a standard "framework" for all the other pages which will be accessible once the user has authenticated with a clean, airy and spacious feel. This will provide styling for standard elements (input boxes, checkboxes, etc...) as well as a given layout, possibly 3 columns (fixed-fluid-fixed) although we leave this to the designer's choice.

We want to stress the importance of the Cloud, as well as make users feel like "this is the place to be if you're a modern, tech savvy health professional". Also of high importance is to show that this is a secure place, where data is accessible from anywhere yet also highly protected.

This project is going to provide long-term work for the winner and possibly those we consider close runner ups, so if you guys are interested in grabbing our attention so you can become our designer of choice, this is your chance!

Standard pages we are looking to receive after the selection process:

* Landing page
* Health Professional Profile Page (personal details, professional details, photo...)
* Patient list / Patient Management page
* Patient profile (details, health details...)
* Generic "item" management page (item refers to documents, images, contacts, etc...)

The logo for the site/product is also up for grabs, and a bonus payment can be given if you provide one that both matches the style of the site whilst being one that could be reused for mobile app icons, etc...

The site name is "vornatik" (all lower-case) for those of you wanting to work on the logo part. As I said before, the logo should contain a component that could be use as the recognisable icon in a mobile phone app. Something that can be easily identified in both the site and the app that connects them together.

vornatik is made up of two parts (vorn + atik), and you might want to consider differentiating them by the use of colour, fonts or however you think appropriate.

New sample screen-shots of the existing functionality have been uploaded to help you mock up some screens.

PLEASE NOTE: This are to be used for content/widget design only! The layout of how these are represented, e.g. accordion, slider, tree, list... is entirely up to you! Don't guide your layout based on these screen-shots, unless you think they are the way to go, of course. 

We want your creative input, so please innovate! :)

Thanks!

Target Market(s)

Health Professionals

Industry/Entity Type

Health

Requirements
Must have
• * A landing page that grabs the users attention but is "different" from the rest of pages (although within the same design/style parameters)

* A generic page framework for the rest of the pages (style guide)
Nice to have
• A modern and clean logo to go with the site. If the logo is selected, this can result in a bonus payment to be decided.

```html
<!DOCTYPE html>
<html lang="en">
<head>
<meta charset="utf-8">
<title>vornatik – Your Patients</title>
<link href="https://fonts.googleapis.com/css2?family=Open+Sans:wght@400;600;700&display=swap" rel="stylesheet">
<style>
:root{
  --blue:#2a63b8;
  --blue-light:#4a86d6;
  --blue-dark:#1d4f9a;
  --ink:#333;
  --muted:#666;
  --line:#dcdcdc;
  --page:#e4e4e4;
  --footer:#d2d2d2;
  --red:#d40d12;
  --pink:#e8a3a3;
  --ad:#d6d6d6;
  --white:#fff;
}
*{box-sizing:border-box;margin:0;padding:0}
html,body{width:1200px;height:840px;overflow:hidden}
body{font-family:"Open Sans",Arial,sans-serif;color:var(--ink);background:var(--page);position:relative;font-size:12px}
.topline{position:absolute;left:0;top:0;width:1200px;height:5px;background:var(--blue)}
.header{position:absolute;left:0;top:5px;width:1200px;height:95px;background:linear-gradient(#fff,#f1f1f1);border-bottom:1px solid #d0d0d0}
.brand{position:absolute;left:120px;top:21px;display:flex;align-items:center;gap:12px}
.brand-mark{width:50px;height:50px;background:var(--blue);border-radius:6px}
.brand-name{font-size:46px;font-weight:600;color:var(--blue-dark);letter-spacing:-1px;line-height:1}
.greeting{position:absolute;right:236px;top:12px;font-size:11px;color:#444;white-space:nowrap}
.logout{position:absolute;left:982px;top:0;width:96px;height:31px;background:var(--blue);color:#fff;border-radius:0 0 3px 3px;display:flex;align-items:center;justify-content:center;gap:8px;font-size:14px}
.logout i{width:15px;height:15px;border-radius:50%;background:var(--red);display:inline-block}
.nav{position:absolute;left:820px;top:52px;display:flex;gap:24px;font-size:18px;color:#444}
.nav span{display:flex;align-items:center;gap:6px}
.nav b{width:14px;height:14px;border-radius:50%;background:#555;display:inline-block;position:relative}
.nav b::after{content:"";position:absolute;left:4px;top:5px;border:3px solid transparent;border-top:4px solid #fff}
.panel{position:absolute;background:#fff;border:1px solid #d3d3d3;border-radius:3px;overflow:hidden}
.panel-title{height:28px;background:linear-gradient(var(--blue-light),var(--blue));color:#fff;font-weight:700;font-size:13px;padding:5px 14px}
.btn-red{background:var(--red);color:#fff;font-size:10px;border-radius:2px;display:inline-block;padding:2px 8px}
/* profile */
.profile{left:120px;top:132px;width:180px;height:285px}
.photo{position:absolute;left:14px;top:42px;width:66px;height:76px;background:linear-gradient(#dfe6ee,#b9c7d6);border:1px solid #ccc}
.last-login{position:absolute;left:96px;top:46px;font-size:12px;line-height:17px;color:#555}
.last-login strong{color:var(--blue-dark)}
.last-login .btn-red{margin-top:2px}
.messages{position:absolute;left:0;top:134px;width:100%}
.messages h4{font-size:12px;color:var(--blue-dark);padding:4px 12px;border-top:1px solid var(--line);border-bottom:1px solid var(--line);display:flex;gap:6px;align-items:center}
.msg{font-size:10px;padding:7px 12px;border-bottom:1px solid var(--line);display:flex;gap:7px;align-items:center;font-weight:700}
.msg.read{font-weight:400}
.msg i{width:10px;height:7px;background:#333;display:inline-block}
.msg.read i{background:none;border:1px solid #555}
.inbox{position:absolute;left:14px;top:252px}
/* social */
.social{left:120px;top:434px;width:180px;height:58px;padding:6px}
.social-dot{position:absolute;left:12px;top:14px;width:26px;height:26px;border-radius:50%;background:#3ea7e6}
.count{position:absolute;left:50px;width:122px;height:22px;border:1px solid #d5d5d5;font-size:10px;font-weight:700;display:flex;justify-content:space-between;padding:3px 8px}
.count span:last-child{color:var(--blue-dark);font-weight:400}
/* manage */
.manage{left:120px;top:502px;width:180px;height:244px}
.manage ul{list-style:none;padding:4px 12px}
.manage li{height:34px;border-bottom:1px solid var(--line);display:flex;align-items:center;gap:12px;font-size:15px;color:#555}
.manage li:last-child{border:0}
.manage li.active{color:var(--blue)}
.manage svg{width:16px;height:16px}
/* table */
.patients{left:317px;top:132px;width:563px;height:614px}
.thead,.row{display:grid;grid-template-columns:161px 192px 113px 66px;align-items:center;padding-left:17px}
.thead{height:40px;background:linear-gradient(#f2f2f2,#e2e2e2);border-bottom:1px solid #ccc;font-size:12px;color:#555}
.thead span{display:flex;align-items:center;gap:6px}
.thead i{width:12px;height:11px;background:#888;display:inline-block;border-radius:2px}
.row{height:38.2px;border-bottom:1px solid #e3e3e3;font-size:11px}
.row:nth-child(even){background:#f6f6f6}
.row .name{font-weight:700;color:var(--blue-dark);white-space:nowrap}
.row .id,.row .dob{color:#444;font-size:11px;white-space:nowrap}
.row.selected{background:var(--pink)!important}
.row.selected .name,.row.selected .id,.row.selected .dob{color:#fff}
.details{width:66px;height:14px;background:var(--blue);color:#fff;font-size:8px;display:flex;align-items:center;justify-content:center;border-radius:1px;white-space:nowrap}
.row.selected .details{background:var(--red)}
.pager{position:absolute;left:18px;top:562px;display:flex;gap:14px;align-items:center;font-size:15px;color:#444}
.pager .arrow{width:22px;height:22px;background:var(--blue);border-radius:2px}
.pager .current{border:1px solid #bbb;padding:0 5px}
.create{position:absolute;right:14px;top:557px;width:118px;height:32px;background:var(--red);color:#fff;font-weight:600;font-size:15px;display:flex;align-items:center;justify-content:center;border-radius:2px}
/* daily numbers */
.daily{left:898px;top:132px;width:180px;height:219px}
.select{position:absolute;left:14px;top:40px;width:146px;height:24px;border:1px solid #bbb;font-size:10px;color:#888;padding:4px 8px;background:#fff}
.select::after{content:"";position:absolute;right:0;top:0;width:16px;height:22px;background:#222}
.field{position:absolute;left:14px;font-size:12px;color:#444;display:flex;align-items:center;width:150px;justify-content:space-between}
.field span:last-child{width:96px;height:24px;border:1px solid #bbb;border-radius:2px;font-size:10px;color:#aaa;padding:4px 6px}
.submit{position:absolute;left:66px;top:180px;width:76px;height:22px;font-size:12px;font-weight:600;display:flex;align-items:center;justify-content:center}
.ad{position:absolute;left:898px;width:180px;background:var(--ad);display:flex;align-items:center;justify-content:center;text-align:center;color:#fff;font-size:38px;font-weight:700;line-height:1.1}
/* footer */
.footer{position:absolute;left:0;top:780px;width:1200px;height:60px;background:var(--footer);border-top:1px solid #c4c4c4}
.footer-links{position:absolute;left:120px;top:23px;font-size:11px;color:#555}
.footer-links span{margin:0 9px;color:#888}
.footer-brand{position:absolute;left:920px;top:14px;display:flex;gap:8px;align-items:center}
.footer-brand i{width:32px;height:32px;background:#fff;border-radius:3px;display:inline-block}
.footer-brand b{font-size:28px;color:#fff;font-weight:600}
</style>
</head>
<body>
<div class="topline"></div>
<header class="header">
  <div class="brand"><span class="brand-mark"></span><span class="brand-name">vornatik</span></div>
  <div class="greeting">Hello, Lena Corvath !</div>
  <nav class="nav"><span>Profile <b></b></span><span>Settings <b></b></span><span>Options</span></nav>
</header>
<div class="logout">Log Out <i></i></div>

<section class="panel profile">
  <div class="panel-title">Dr. Lena Corvath</div>
  <div class="photo" role="img" aria-label="Doctor profile photo"></div>
  <div class="last-login"><strong>Last Login</strong><br>20 Jan 2012<br><span class="btn-red">Edit Profile</span></div>
  <div class="messages">
    <h4><svg width="12" height="9"><rect width="12" height="9" fill="#2a63b8"/></svg>Messages</h4>
    <div class="msg"><i></i>Hello lena corvath...</div>
    <div class="msg"><i></i>Hello lena corvath...</div>
    <div class="msg read"><i></i>Hello lena corvath...</div>
  </div>
  <span class="btn-red inbox">Go to inbox</span>
</section>

<section class="panel social">
  <span class="social-dot"></span>
  <div class="count" style="top:5px"><span>Following</span><span>1,059</span></div>
  <div class="count" style="top:30px"><span>Followers</span><span>2,000</span></div>
</section>

<section class="panel manage">
  <div class="panel-title">Manage Profile</div>
  <ul>
    <li><svg viewBox="0 0 16 16"><path d="M8 1 1 8h2v7h4v-4h2v4h4V8h2z" fill="#666"/></svg>Home</li>
    <li class="active"><svg viewBox="0 0 16 16"><circle cx="5" cy="5" r="3" fill="#2a63b8"/><circle cx="11" cy="5" r="3" fill="#2a63b8"/><path d="M0 14c0-4 10-4 10 0zM8 14c0-4 8-4 8 0z" fill="#2a63b8"/></svg>Patients</li>
    <li><svg viewBox="0 0 16 16"><circle cx="8" cy="6" r="4" fill="none" stroke="#666" stroke-width="2"/><path d="M8 10v6" stroke="#666" stroke-width="2"/></svg>Professionals</li>
    <li><svg viewBox="0 0 16 16"><path d="M1 3h6v11H1zM9 3h6v11H9z" fill="none" stroke="#666" stroke-width="1.5"/></svg>Studies</li>
    <li><svg viewBox="0 0 16 16"><rect x="2" y="1" width="12" height="14" fill="none" stroke="#666" stroke-width="1.5"/><path d="M5 6h6M5 9h6M5 12h4" stroke="#666"/></svg>Surveys</li>
    <li><svg viewBox="0 0 16 16"><path d="M2 14l2-5 8-8 3 3-8 8z" fill="#666"/></svg>Designer</li>
  </ul>
</section>

<section class="panel patients">
  <div class="panel-title">Your Patients</div>
  <div class="thead"><span><i></i>Patients Name</span><span><i></i>ID</span><span><i></i>D.O.B</span><span><i></i>Details</span></div>
  <div class="rows">
    <div class="row"><span class="name">Tomas Brevik</span><span class="id">tomasbrevik@vornatik.com</span><span class="dob">03-Nov-1975</span><span class="details">Full Details</span></div>
    <div class="row"><span class="name">Lena Corvath</span><span class="id">lena@vornatik.com</span><span class="dob">03-Nov-1985</span><span class="details">Full Details</span></div>
    <div class="row"><span class="name">Ines Valdoro</span><span class="id">ines@vornatik.com</span><span class="dob">03-Nov-1970</span><span class="details">Full Details</span></div>
    <div class="row selected"><span class="name">Marco Corvath</span><span class="id">marco@vornatik.com</span><span class="dob">03-Nov-1960</span><span class="details">Full Details</span></div>
    <div class="row"><span class="name">Tomas Brevik</span><span class="id">tomasbrevik@vornatik.com</span><span class="dob">03-Nov-1975</span><span class="details">Full Details</span></div>
    <div class="row"><span class="name">Lena Corvath</span><span class="id">lena@vornatik.com</span><span class="dob">03-Nov-1985</span><span class="details">Full Details</span></div>
    <div class="row"><span class="name">Ines Valdoro</span><span class="id">ines@vornatik.com</span><span class="dob">03-Nov-1970</span><span class="details">Full Details</span></div>
    <div class="row"><span class="name">Marco Corvath</span><span class="id">marco@vornatik.com</span><span class="dob">03-Nov-1960</span><span class="details">Full Details</span></div>
    <div class="row"><span class="name">Tomas Brevik</span><span class="id">tomasbrevik@vornatik.com</span><span class="dob">03-Nov-1975</span><span class="details">Full Details</span></div>
    <div class="row"><span class="name">Lena Corvath</span><span class="id">lena@vornatik.com</span><span class="dob">03-Nov-1985</span><span class="details">Full Details</span></div>
    <div class="row"><span class="name">Ines Valdoro</span><span class="id">ines@vornatik.com</span><span class="dob">03-Nov-1970</span><span class="details">Full Details</span></div>
    <div class="row"><span class="name">Marco Corvath</span><span class="id">marco@vornatik.com</span><span class="dob">03-Nov-1960</span><span class="details">Full Details</span></div>
  </div>
  <div class="pager">
    <svg class="arrow" viewBox="0 0 22 22"><rect width="22" height="22" rx="2" fill="#2a63b8"/><path d="M13 6l-5 5 5 5" stroke="#fff" stroke-width="2.5" fill="none"/></svg>
    <span class="current">1</span><span>2</span><span>3</span><span>4</span><span>5</span>
    <svg class="arrow" viewBox="0 0 22 22"><rect width="22" height="22" rx="2" fill="#2a63b8"/><path d="M9 6l5 5-5 5" stroke="#fff" stroke-width="2.5" fill="none"/></svg>
  </div>
  <div class="create">Create New</div>
</section>

<section class="panel daily">
  <div class="panel-title">My Daily Numbers</div>
  <div class="select">Blood Pressure</div>
  <div class="field" style="top:80px"><span>Diastolic</span><span>mmHg</span></div>
  <div class="field" style="top:112px"><span>Systolic</span><span>mmHg</span></div>
  <div class="field" style="top:144px"><span>Date</span><span>DD/MM/YYYY</span></div>
  <span class="btn-red submit">Submit</span>
</section>

<div class="ad" style="top:372px;height:219px">Add<br>Space</div>
<div class="ad" style="top:610px;height:137px">Add<br>Space</div>

<footer class="footer">
  <div class="footer-links">About Us<span>|</span>Pricing<span>|</span>FAQ<span>|</span>Contact Us</div>
  <div class="footer-brand"><i></i><b>vornatik</b></div>
</footer>
</body>
</html>
```